Half page (a5) ad for a company

I need a design for an ad for a company to be published in a conference catalogue. Please find enclosed the logo for a company. The company is providing health screening services. Ad should be subtle and minimalistic, i.e. logo in the centre and a phrase saying: "Be in charge of your own health" and the website vantolix.co.uk. Also please find enclosed guidlines for colours and fonts to be used.

```html
<!DOCTYPE html>
<html lang="en">
<head>
<meta charset="UTF-8">
<title>Vantolix Private – Conference Ad</title>
<link href="https://fonts.googleapis.com/css2?family=Montserrat:wght@400;600&display=swap" rel="stylesheet">
<style>
  :root {
    --page-bg: #e0e0e0;
    --ad-black: #000000;
    --ad-white: #ffffff;
    --brand-red: #e30613;
    --brand-red-deep: #b00a14;
    --text-dark: #0a0a0a;
  }
  * { margin: 0; padding: 0; box-sizing: border-box; }
  html, body {
    width: 1200px;
    height: 1200px;
    overflow: hidden;
    background: var(--page-bg);
    font-family: "Montserrat", sans-serif;
  }
  .ad {
    position: absolute;
    left: 204px;
    top: 40px;
    width: 792px;
    height: 1120px;
    background: var(--ad-white);
  }
  .ad__brand-panel {
    position: absolute;
    left: 0; top: 0;
    width: 100%;
    height: 661px;
    background: var(--ad-black);
  }
  .brand {
    position: absolute;
    left: 0; right: 0;
    top: 200px;
    display: flex;
    flex-direction: column;
    align-items: center;
    gap: 60px;
  }
  .brand__dot {
    width: 90px;
    height: 90px;
    border-radius: 50%;
    background: var(--brand-red);
  }
  .brand__name {
    color: var(--brand-red);
    font-weight: 400;
    font-size: 66px;
    letter-spacing: 0.5px;
    white-space: nowrap;
    line-height: 1;
  }
  .headline {
    position: absolute;
    left: 0; right: 0;
    top: 722px;
    text-align: center;
    font-weight: 600;
    font-size: 63px;
    line-height: 82px;
  }
  .headline__lead { display: block; color: var(--text-dark); }
  .headline__accent { display: block; color: var(--brand-red); }
  .web-button {
    position: absolute;
    left: 266px;
    top: 962px;
    width: 262px;
    height: 56px;
    border-radius: 28px;
    background: linear-gradient(180deg, var(--brand-red) 0%, var(--brand-red) 55%, var(--brand-red-deep) 100%);
    color: var(--ad-white);
    font-weight: 600;
    font-size: 26px;
    display: flex;
    align-items: center;
    justify-content: center;
  }
</style>
</head>
<body>
  <main class="ad">
    <section class="ad__brand-panel">
      <div class="brand">
        <div class="brand__dot"></div>
        <div class="brand__name">Vantolix Private</div>
      </div>
    </section>
    <h1 class="headline">
      <span class="headline__lead">Be in charge of</span>
      <span class="headline__accent">your own health</span>
    </h1>
    <div class="web-button">vantolix.co.uk</div>
  </main>
</body>
</html>
```